Medical Practice Brochure Design Project

We are a medical practice in Denver, Colorado and we need to design a brochure to promote one subset of services we offer. We perform Office of Civic Harbors (OCH) physical exams and also perform OCH drug testing onsite and want a brochure that outlines these services. This brochure will be used a part of a marketing package to promote this service to businesses that employ individuals that drive commercial vehicles.
Updates

Project Deadline Extended Reason: I am going extend the deadline for submissions. Ending on a Sunday is going to limit last minute submissions. As a trade off, I am going to guarantee this project. Thanks for all the submissions. Added Thursday, October 09, 2014

(omitted with map) Market(s)

human resource managers, companies that deploy commercial vehicles (i.e. trucks and tractor trailers), independent drivers / contractors

Industry/Entity Type

Medical

Font styles to use
Sans Serif

Colors
0455a3

Requirements
Must have
• Our logo, our web address (halvoraclinic.com), our phone number and fax number, professional look and feel, layout be a trifold 8.5x11 (see templates), map to our location (see attached for example).
Nice to have
• Our logo (larkspur family medicine) should not be the focus of the brochure. Text items that should stand out should be "OCH Examination", "OCH Drug Testing" and "FGWAS Certified Providers", our phone number, and our web address. We also will have the ability to have clients schedule appointment online through our website which should be indicated in the brochure in a prominent manner.
Should not have
• no images of crosses, no images of syringes

```html
<!DOCTYPE html>
<html lang="en">
<head>
<meta charset="utf-8">
<title>Larkspur Family Medicine – OCH Services Brochure</title>
<link rel="stylesheet" href="https://fonts.googleapis.com/css2?family=Arimo:wght@700&family=Saira+Semi+Condensed:wght@300;400&family=Montserrat:wght@700&display=swap">
<style>
  :root {
    --page-blue: #0b5cf4;
    --panel-blue: #2a6bf8;
    --exam-blue: #0a33ad;
    --drug-navy: #1a3d68;
    --note-navy: #0a33a8;
    --note-frame: #2a6bf8;
    --white: #ffffff;
    --logo-blue: #1a56d8;
    --map-tone: #cfe6ef;
  }
  html, body {
    margin: 0;
    padding: 0;
    overflow: hidden;
  }
  .brochure {
    position: relative;
    width: 1200px;
    height: 931px;
    background: var(--page-blue);
    overflow: hidden;
    font-family: "Arimo", Arial, sans-serif;
    font-weight: 700;
    color: var(--white);
  }
  .info-bar {
    position: absolute;
    left: 21px;
    width: 362px;
    background: var(--panel-blue);
  }
  .info-bar--1 { top: 74px; height: 94px; }
  .info-bar--2 { top: 175px; height: 48px; }
  .info-bar--3 { top: 234px; height: 47px; }
  .info-bar--4 { top: 290px; height: 48px; }

  .location-map {
    position: absolute;
    left: 443px;
    top: 106px;
    width: 317px;
    height: 266px;
    background: var(--map-tone);
    border: 1px solid #1b2a55;
    box-sizing: border-box;
  }

  .brand {
    position: absolute;
    left: 842px;
    top: 86px;
    width: 305px;
    height: 125px;
    background: var(--white);
    display: flex;
    flex-direction: column;
    align-items: center;
    justify-content: center;
    font-family: "Montserrat", Arial, sans-serif;
    font-weight: 700;
    color: var(--logo-blue);
    text-align: center;
    line-height: 1;
    white-space: nowrap;
  }
  .brand__name { font-size: 46px; letter-spacing: 1px; }
  .brand__line { font-size: 22px; margin-top: 8px; letter-spacing: 0.5px; }

  .service {
    position: absolute;
    left: 810px;
    width: 369px;
    overflow: hidden;
    font-family: "Saira Semi Condensed", "Roboto Condensed", "Arial Narrow", sans-serif;
    font-weight: 300;
    color: var(--white);
  }
  .service--exam { top: 262px; height: 171px; background: var(--exam-blue); }
  .service--drug { top: 443px; height: 172px; background: var(--drug-navy); }
  .service--cert { top: 624px; height: 173px; background: var(--panel-blue); }
  .service__title,
  .service__sub {
    position: absolute;
    white-space: nowrap;
    line-height: 1;
    font-weight: 300;
  }
  .service__title { font-size: 72px; }
  .service__sub { font-size: 31px; }
  .service--exam .service__title { left: 72px; top: 29px; }
  .service--exam .service__sub { right: 75px; top: 108px; }
  .service--drug .service__title { left: 60px; top: 27px; }
  .service--drug .service__sub { right: 70px; top: 106px; }
  .service--cert .service__title { left: 64px; top: 30px; }
  .service--cert .service__sub { left: 64px; top: 110px; }

  .directions {
    position: absolute;
    left: 411px;
    top: 521px;
    width: 364px;
    height: 264px;
    background: var(--note-frame);
  }
  .directions__body {
    position: absolute;
    left: 0;
    top: 18px;
    width: 364px;
    height: 227px;
    box-sizing: border-box;
    background: var(--note-navy);
    padding: 29px 12px 0 17px;
    font-size: 12px;
    line-height: 31.5px;
    text-transform: uppercase;
    white-space: nowrap;
  }
  .directions__body p { margin: 0; }

  .contact {
    position: absolute;
    left: 21px;
    top: 567px;
    width: 362px;
    height: 341px;
  }
  .contact__shape {
    position: absolute;
    inset: 0;
  }
  .contact__text {
    position: absolute;
    left: 0;
    top: 63px;
    width: 362px;
    text-align: center;
    font-size: 19px;
    line-height: 37.8px;
    white-space: nowrap;
  }
  .contact__text p { margin: 0; }
</style>
</head>
<body>
<main class="brochure">
  <div class="info-bar info-bar--1"></div>
  <div class="info-bar info-bar--2"></div>
  <div class="info-bar info-bar--3"></div>
  <div class="info-bar info-bar--4"></div>

  <div class="location-map" role="img" aria-label="Street map showing the clinic on the south side of Meadowlark Road, east of the Rt 9 interchange"></div>

  <div class="brand" aria-label="Larkspur Family Medicine">
    <span class="brand__name">LARKSPUR</span>
    <span class="brand__line">FAMILY MEDICINE</span>
  </div>

  <section class="service service--exam">
    <span class="service__title">OCH</span>
    <span class="service__sub">Examination</span>
  </section>
  <section class="service service--drug">
    <span class="service__title">OCH Drug</span>
    <span class="service__sub">Testing</span>
  </section>
  <section class="service service--cert">
    <span class="service__title">FGWAS</span>
    <span class="service__sub">Certified Providers</span>
  </section>

  <section class="directions">
    <div class="directions__body">
      <p>Our offices is located the south side</p>
      <p>of Meadowlark Road approxmately</p>
      <p>one-half miles east of the Rt 9/Meadowlark</p>
      <p>road intersection(exit 42 of Rt 9).</p>
      <p>Our offices is in a retail space near the</p>
      <p>Green Basket Market grocers store</p>
    </div>
  </section>

  <section class="contact">
    <svg class="contact__shape" width="362" height="341" viewBox="0 0 362 341" aria-hidden="true">
      <polygon points="0,51 362,0 362,286 0,341" fill="#2a6bf8"/>
    </svg>
    <div class="contact__text">
      <p>Our Address</p>
      <p>4815 E Meadowlark Rd</p>
      <p>Juniper Hollow CO, 80147</p>
      <p>Phone Number (555) 014-2286</p>
      <p>FAX Number &nbsp;&nbsp;&nbsp;&nbsp;(555) 014-2290</p>
      <p>www.halvoraclinic.com</p>
    </div>
  </section>
</main>
</body>
</html>
```